New business card/stationary for a consulting company

I am looking for a clean and very professional looking business card for my consulting company as well as corresponding stationary. I am uploading our logo. I like simple and powerful for the feel. No graphics but I am open on everything else. Below is my contact information but would like the final to be in a version I can add my employees information into and print. Thank you.

Daniel Whitcombe
dan@fernlowadvisory.com
2837 North 9th Avenue, Summit Floor, Brookhollow, Ohio 60483
www.fernlowadvisory.com

Industry/Entity Type

Consulting

Contact Information for Business Card

Daniel Whitcombe
dan@fernlowadvisory.com
www.fernlowadvisory.com

Font styles to use
Serif
Sans Serif

Requirements
Must have
• Our logo and the business card details.
Nice to have
• our website www.fernlowadvisory.com

```html
<!DOCTYPE html>
<html lang="en">
<head>
<meta charset="utf-8">
<title>Fernlow Advisory – Business Card</title>
<link rel="stylesheet" href="https://fonts.googleapis.com/css2?family=Cinzel:wght@400;700&family=Lato:wght@300;400&display=swap">
<style>
  :root {
    --navy: #272560;
    --paper: #ffffff;
    --contact: #c9c9d8;
    --name: #ffffff;
  }
  * { margin: 0; padding: 0; box-sizing: border-box; }
  html, body {
    width: 1200px;
    height: 681px;
    overflow: hidden;
    background: var(--paper);
  }
  .card {
    position: relative;
    width: 1200px;
    height: 681px;
    background: var(--paper);
    overflow: hidden;
  }
  .brand {
    position: absolute;
    top: 0;
    left: 0;
    width: 1200px;
    height: 286px;
  }
  .brand-square {
    position: absolute;
    left: 533px;
    top: 34px;
    width: 134px;
    height: 134px;
    background: var(--navy);
  }
  .brand-name {
    position: absolute;
    left: 0;
    width: 1200px;
    top: 200px;
    text-align: center;
    font-family: "Cinzel", serif;
    font-weight: 400;
    font-size: 62px;
    line-height: 1;
    letter-spacing: 8px;
    color: var(--navy);
  }
  .divider {
    position: absolute;
    left: 0;
    top: 286px;
    width: 1200px;
    height: 10px;
    background: var(--navy);
  }
  .details {
    position: absolute;
    left: 0;
    top: 312px;
    width: 1200px;
    height: 369px;
    background: var(--navy);
  }
  .person-name {
    position: absolute;
    left: 66px;
    top: 44px;
    font-family: "Cinzel", serif;
    font-weight: 700;
    font-size: 54px;
    line-height: 1;
    letter-spacing: 7px;
    color: var(--name);
  }
  .contact {
    position: absolute;
    left: 61px;
    top: 116px;
    list-style: none;
    font-family: "Lato", sans-serif;
    font-weight: 300;
    font-size: 40px;
    line-height: 51px;
    color: var(--contact);
  }
</style>
</head>
<body>
  <main class="card">
    <header class="brand">
      <div class="brand-square" aria-hidden="true"></div>
      <h1 class="brand-name">FERNLOW ADVISORY</h1>
    </header>
    <div class="divider" aria-hidden="true"></div>
    <section class="details">
      <h2 class="person-name">Daniel Whitcombe</h2>
      <ul class="contact">
        <li>dan@fernlowadvisory.com</li>
        <li>2837 North 9th Avenue, Summit Floor,</li>
        <li>Brookhollow, Ohio 60483</li>
        <li>www.fernlowadvisory.com</li>
      </ul>
    </section>
  </main>
</body>
</html>
```